Air Conditioning Advertisement

I am looking to design an ad for my HVAC company. The name of my company is Pine Hollow Cooling INC. We provide 24/7 emergency service.
Image- Ductless air conditioning unit & central air conditioning unit
Website- www.brisktundrahvac.example
company phone number- 516-387-5924

I would like an ad advertising our spring special. The spring special is $750 off a new Central Air conditioning or ductlesss air conditioning installation.

Our other special is $100 Central AC Tune up.

I attached my logo.

Target Market(s)

Home owners & small businesses

Industry/Entity Type

Air conditioning, Refrigeration & Heating

Colors
0054AA
0677BA
7BADD7
CADEEF
E8F1F8
EE7325
F08F49
F5BC92
FAE3D3
FDF4ED

Requirements
Must have
• Pictures of ductless air conditioning and central air conditioning unit.
Nice to have
• Id like to have an ad that incorporates my company colors & logos. I want this ad to stand out & show what we are offering. The ad should display, briefly say the importance of comfort in your home.

```html
<!DOCTYPE html>
<html lang="en">
<head>
<meta charset="utf-8">
<title>Pine Hollow Cooling INC – Spring Special</title>
<link rel="stylesheet" href="https://fonts.googleapis.com/css2?family=Oswald:wght@400;500;600&family=Poppins:wght@600&display=swap">
<style>
  :root {
    --orange: #f26b10;
    --orange-light: #ff9a3c;
    --floor-blue: #0838d8;
    --sticker-blue: #0b4db3;
    --white: #ffffff;
    --ink: #3d3d3d;
    --unit-grey: #dfe2e5;
    --unit-shade: #a9aeb4;
    --unit-vent: #c9ccd0;
  }
  * { margin: 0; padding: 0; box-sizing: border-box; }
  html, body { width: 1200px; height: 1200px; overflow: hidden; }
  body { font-family: "Oswald", sans-serif; }
  .ad {
    position: relative;
    width: 1200px;
    height: 1200px;
    background: radial-gradient(circle at 620px 620px, var(--orange-light) 0%, var(--orange) 62%);
    overflow: hidden;
  }
  .floor {
    position: absolute;
    left: 0; right: 0; top: 794px; bottom: 0;
    background: linear-gradient(180deg, #0a3fe6 0%, var(--floor-blue) 100%);
  }
  .headline {
    position: absolute;
    left: 0; top: 0;
    width: 1200px; height: 660px;
  }
  .headline text {
    font-family: "Poppins", sans-serif;
    font-weight: 600;
    fill: var(--white);
    stroke: var(--sticker-blue);
    stroke-width: 36px;
    stroke-linejoin: round;
    paint-order: stroke fill;
  }
  .unit-outdoor {
    position: absolute;
    left: 128px; top: 480px;
    width: 428px; height: 387px;
    border-radius: 10px;
    background:
      radial-gradient(circle at 62% 52%, var(--unit-vent) 0%, var(--unit-grey) 34%, transparent 35%),
      linear-gradient(90deg, var(--unit-shade) 0%, #8d9299 14%, var(--unit-grey) 17%, var(--white) 70%, var(--unit-grey) 100%);
    box-shadow: 0 18px 24px rgba(0, 0, 40, 0.25);
  }
  .unit-ductless {
    position: absolute;
    left: 489px; top: 641px;
    width: 500px; height: 170px;
    border-radius: 12px;
    background: linear-gradient(180deg, var(--white) 0%, #f2f3f4 62%, var(--unit-vent) 63%, var(--unit-grey) 100%);
    box-shadow: 0 14px 20px rgba(0, 0, 40, 0.22);
    display: flex;
    align-items: flex-start;
    justify-content: center;
    padding-top: 36px;
  }
  .unit-ductless .brand {
    font-family: "Oswald", sans-serif;
    font-weight: 600;
    font-size: 28px;
    color: var(--sticker-blue);
    letter-spacing: 1px;
    text-transform: uppercase;
  }
  .service-note {
    position: absolute;
    left: 503px; top: 846px;
    font-size: 30px;
    font-weight: 500;
    color: var(--orange);
    text-transform: uppercase;
    white-space: nowrap;
  }
  .offer-stroke {
    position: absolute;
    left: 128px; top: 912px;
    width: 972px; height: 118px;
  }
  .offer {
    position: absolute;
    left: 232px; top: 928px;
    display: flex;
    align-items: center;
    gap: 24px;
    height: 90px;
  }
  .offer .amount {
    font-size: 66px;
    font-weight: 600;
    color: var(--orange);
    line-height: 1;
    white-space: nowrap;
  }
  .offer .detail {
    font-size: 27px;
    font-weight: 400;
    color: var(--ink);
    line-height: 1.2;
    text-transform: uppercase;
    white-space: nowrap;
  }
  .contact {
    position: absolute;
    left: 0; right: 0; top: 1058px;
    text-align: center;
    font-size: 48px;
    font-weight: 500;
    color: var(--white);
    letter-spacing: 1px;
    text-transform: uppercase;
    white-space: nowrap;
  }
  .contact .divider { margin: 0 14px; }
</style>
</head>
<body>
<main class="ad">
  <div class="floor"></div>

  <svg class="headline" viewBox="0 0 1200 660" aria-label="Spring Special">
    <text x="222" y="395" font-size="150" transform="rotate(-6 222 395)">Spring</text>
    <text x="590" y="560" font-size="140" transform="rotate(-12 590 560)">Special</text>
  </svg>

  <div class="unit-outdoor" role="img" aria-label="Central air conditioning outdoor condenser unit"></div>

  <div class="unit-ductless" role="img" aria-label="Ductless wall-mounted air conditioning unit">
    <span class="brand">Pine Hollow Cooling INC</span>
  </div>

  <p class="service-note">We provide 24/7 emergency service</p>

  <svg class="offer-stroke" viewBox="0 0 972 118" preserveAspectRatio="none" aria-hidden="true">
    <path d="M24 20 L120 8 L300 14 L520 6 L760 12 L940 8 L928 30 L966 44 L940 58 L972 76 L944 90 L958 110 L720 104 L480 114 L240 106 L60 112 L20 100 L36 84 L0 68 L30 54 L8 36 Z" fill="#ffffff"/>
  </svg>

  <div class="offer">
    <span class="amount">$750 OFF</span>
    <span class="detail">A new central air conditioning or<br>ductlesss air conditioning installation</span>
  </div>

  <p class="contact">516-387-5924<span class="divider">|</span>www.brisktundrahvac.example</p>
</main>
</body>
</html>
```